Design Challege - Simplify a Complex Message

We have a new website design, but one of the pages presents a particular problem.

Our company does ERP implementations. We have developed a proprietary approach to these implementations based on the idea that you must get eight (and only eight) things right. These eight things are listed below, summarized in one or two words each:

1. Value
2. Capability
3. Functionality
4. Data
5. Technology
6. Change Leadership
7. Quality
8. Governance

Each of these eight things can be summarized in a short paragraph, but when you combine all eight summaries with a brief introductory text, the result is a lot of text - so much text that the casual surfer may be overwhelmed by it.

The winning design will find an engaging way to present the information in a way that presents a high-level summary, using icons and one- or two-word descriptions above but revealing more information when clicked.

Our current design for this information, with a paragraph describing the eight elements in a table, is included as an upload in PDF and Microsoft Word formats. We are looking for a creative way to display these eight things, showing the detail only when the user wants to see it.

The website is being built in WordPress, using Elementor as a page builder.

We will implement (code) the page, but the winner will be asked to specify the widget or other add-in if one is required.

The design does not need to include a header or footer, we have those.

Target Market(s)

Business executives working in technology

Industry/Entity Type

Any

Number of Pages Required

1 page

Font styles to use
Sans Serif

Requirements
Must have
• A design for the body of the page, but not the header or footer.
Nice to have
• Unique icons or images appropriate for each of the eight things.
Should not have
• A lot of text on one page

```html
<!DOCTYPE html>
<html lang="en">
<head>
<meta charset="utf-8">
<title>Eight Essentials Wheel</title>
<link rel="stylesheet" href="https://fonts.googleapis.com/css2?family=Open+Sans:wght@400;600&display=swap">
<style>
  :root {
    --page-bg: #ffffff;
    --wheel-light: #3b93d3;
    --wheel-mid: #2275c0;
    --wheel-deep: #1461b0;
    --wheel-shadow: rgba(20, 40, 70, 0.28);
    --label-ink: #ffffff;
  }
  html, body {
    margin: 0;
    padding: 0;
    width: 1200px;
    height: 675px;
    overflow: hidden;
    background: var(--page-bg);
    font-family: "Open Sans", sans-serif;
  }
  .stage {
    position: relative;
    width: 1200px;
    height: 675px;
  }
  .essentials-wheel {
    position: absolute;
    inset: 0;
    width: 1200px;
    height: 675px;
  }
  .wheel-slices {
    filter: drop-shadow(0 6px 10px var(--wheel-shadow));
  }
  .stop-light { stop-color: var(--wheel-light); }
  .stop-mid { stop-color: var(--wheel-mid); }
  .stop-deep { stop-color: var(--wheel-deep); }
  .slice-number {
    font-family: "Open Sans", sans-serif;
    font-size: 10px;
    font-weight: 400;
    letter-spacing: 1px;
    fill: var(--label-ink);
    opacity: 0.8;
    text-anchor: middle;
  }
  .slice-label {
    font-family: "Open Sans", sans-serif;
    font-size: 11.5px;
    font-weight: 600;
    fill: var(--label-ink);
    text-anchor: middle;
  }
</style>
</head>
<body>
<main class="stage">
  <svg class="essentials-wheel" viewBox="0 0 1200 675" xmlns="http://www.w3.org/2000/svg">
    <defs>
      <linearGradient id="wheel-tone" x1="0" y1="0" x2="1" y2="1">
        <stop offset="0" class="stop-light"/>
        <stop offset="0.5" class="stop-mid"/>
        <stop offset="1" class="stop-deep"/>
      </linearGradient>
      <mask id="slice-gaps" maskUnits="userSpaceOnUse" x="0" y="0" width="1200" height="675">
        <rect x="0" y="0" width="1200" height="675" fill="#fff"/>
        <g stroke="#000" stroke-width="16">
          <line x1="370" y1="337.5" x2="830" y2="337.5"/>
          <line x1="600" y1="107" x2="600" y2="568"/>
          <line x1="437" y1="174.5" x2="763" y2="500.5"/>
          <line x1="763" y1="174.5" x2="437" y2="500.5"/>
        </g>
        <circle cx="600" cy="337.5" r="15" fill="#000"/>
      </mask>
    </defs>
    <g class="wheel-slices" role="img" aria-label="Photo of a business team meeting in an office, tinted blue, split into eight wheel segments">
      <circle cx="600" cy="337.5" r="202" fill="url(#wheel-tone)" mask="url(#slice-gaps)"/>
    </g>

    <g class="slice-labels">
      <g class="slice" transform="translate(653.6 208.2)">
        <text class="slice-number" y="-6">01</text>
        <text class="slice-label" y="10">Value</text>
      </g>
      <g class="slice" transform="translate(729.3 283.9)">
        <text class="slice-number" y="-6">02</text>
        <text class="slice-label" y="10">Capability</text>
      </g>
      <g class="slice" transform="translate(729.3 391.1)">
        <text class="slice-number" y="-6">03</text>
        <text class="slice-label" y="10">Functionality</text>
      </g>
      <g class="slice" transform="translate(653.6 466.8)">
        <text class="slice-number" y="-6">04</text>
        <text class="slice-label" y="10">Data</text>
      </g>
      <g class="slice" transform="translate(546.4 466.8)">
        <text class="slice-number" y="-6">05</text>
        <text class="slice-label" y="10">Technology</text>
      </g>
      <g class="slice" transform="translate(470.7 391.1)">
        <text class="slice-number" y="-12">06</text>
        <text class="slice-label" y="4">Change</text>
        <text class="slice-label" y="18">Leadership</text>
      </g>
      <g class="slice" transform="translate(470.7 283.9)">
        <text class="slice-number" y="-6">07</text>
        <text class="slice-label" y="10">Quality</text>
      </g>
      <g class="slice" transform="translate(546.4 208.2)">
        <text class="slice-number" y="-6">08</text>
        <text class="slice-label" y="10">Governance</text>
      </g>
    </g>
  </svg>
</main>
</body>
</html>
```